Need label design for car cleaning spray bottle, big opportunity for repeat work

This is the first label design for a large assortment of car cleaning products. This design will be vital as it will set the design style for the remaining products. There is large opportunity for repeat work to the winning designer. For this first product we plan to call it "Interior Cleaner". We have the template label which we have attached to the project. The product is geared towards the market of Volmara car owners, and our logo also utilizes a similar font to what Volmara's company font uses.

We are looking to only update the design/format of the label. We will keep all text the same or modify it once the design is final. We will need to use our brand logo (attached).

We are looking for a minimalistic style design. Currently the label reads horizontally but we have noticed that the most successful brands that sell online have a vertical style design. We have attached some examples of brands such as "Gleam Bastion" and "Pivlo" which sell primarily on shopvendrix.com and have tens of thousands of reviews. We'd like to try and copy this label format as it seems very successful for these brands.

We are big fans of the minimal style that the brand "AutoZell" uses. Their label design emphasizes the name of the particular product in black text on a white background. The remainder of the label is color coded, and all of their products have a different color code while following the same diagonal design style. See attached examples.

So that being said, we would like to combine these 2 concepts, vertical alignment style with the minimalistic label design.

We are thinking of making the entire label white, and having an accent color like 1 large stripe that goes across the bottle, it would be an iconic part of the design as we will repeat this design across multiple products, similar to the AutoZell brand bundle example we attached. This specific product will be pink liquid (as you can tell the accent color is pink on the label).

We'd like to add a dynamic QR code (can use placeholder) on the label so customers can be directed to our website easily or any other page we choose in the future. We will also need a UPC barcode label (can use placeholder)

Target Market(s)

Volmara car owners

Industry/Entity Type

Car Detailing Products

Font styles to use
Sans Serif

Colors
E54698
E96AAD
F1A4CE
F9D9EA
FCEFF6

Requirements
Must have
• minimalistic design
Should not have
• no designs similar to brands like polish crew, dravonels, or any older brands in the category

```html
<!DOCTYPE html>
<html lang="en">
<head>
<meta charset="utf-8">
<title>Kestrane Interior Cleaner – Label</title>
<link rel="stylesheet" href="https://fonts.googleapis.com/css2?family=Montserrat:wght@300;400;500;700;800&display=swap">
<style>
  :root{
    --stage:#cfcfd1;
    --label-black:#1c1b1d;
    --label-deep:#121113;
    --pink:#e54698;
    --pink-mid:#e96aad;
    --pink-soft:#f1a4ce;
    --pink-pale:#f9d9ea;
    --silver:#c8c8ce;
    --silver-dark:#8e8e96;
    --white:#f4f4f6;
  }
  *{margin:0;padding:0;box-sizing:border-box}
  html,body{width:1200px;height:800px;overflow:hidden}
  body{
    background:radial-gradient(ellipse at center,#e2e2e3 0%,var(--stage) 55%,#b4b4b6 100%);
    font-family:"Montserrat",sans-serif;
    position:relative;
  }
  .label{
    position:absolute;left:445px;top:30px;width:310px;height:740px;
    background:var(--label-black);overflow:hidden;
  }
  .label__texture{
    position:absolute;inset:0;
    background:radial-gradient(ellipse at 30% 40%,#2a2428 0%,var(--label-black) 55%,var(--label-deep) 100%);
  }
  .brand{
    position:absolute;top:22px;left:0;right:0;
    display:flex;align-items:center;gap:8px;
  }
  .brand__rule{height:1.5px;background:var(--pink)}
  .brand__rule--left{width:40px;margin-left:30px}
  .brand__rule--right{flex:1}
  .brand__name{
    font-weight:500;font-size:19px;letter-spacing:2px;color:var(--white);
    white-space:nowrap;
  }
  .brand__name sup{font-size:8px;letter-spacing:0}
  .product-name{
    position:absolute;bottom:220px;left:106px;
    display:flex;align-items:flex-end;gap:4px;
  }
  .product-name__line{
    writing-mode:vertical-rl;transform:rotate(180deg);white-space:nowrap;line-height:.8;
  }
  .product-name__type{
    font-weight:300;font-size:43px;letter-spacing:.5px;color:var(--pink);
  }
  .product-name__main{
    font-weight:400;font-size:84px;letter-spacing:0;
    background:linear-gradient(90deg,var(--silver-dark),var(--silver) 60%,#e6e6ea);
    -webkit-background-clip:text;background-clip:text;color:transparent;
  }
  .swoosh{position:absolute;inset:0;width:310px;height:740px}
  .benefits{
    position:absolute;top:592px;left:44px;width:214px;
    background:var(--label-black);
    border:3px solid var(--pink-mid);border-radius:6px;
    padding:6px 8px;list-style:none;
  }
  .benefits li{
    font-size:9.5px;font-weight:800;color:var(--white);line-height:1.6;
    letter-spacing:.2px;white-space:nowrap;
  }
  .benefits li::before{
    content:"";display:inline-block;width:4px;height:4px;border-radius:50%;
    background:var(--pink-soft);margin-right:4px;vertical-align:2px;
  }
  .benefits .soft{font-weight:500}
  .net-contents{
    position:absolute;top:694px;left:0;right:0;text-align:center;
    font-size:8px;font-weight:500;color:var(--silver);letter-spacing:.3px;
  }
</style>
</head>
<body>
  <section class="label" aria-label="Kestrane Interior Cleaner label">
    <div class="label__texture" role="img" aria-label="Faint pink topographic contour lines on black"></div>

    <header class="brand">
      <span class="brand__rule brand__rule--left"></span>
      <span class="brand__name">KESTRANE<sup>®</sup></span>
      <span class="brand__rule brand__rule--right"></span>
    </header>

    <h1 class="product-name">
      <span class="product-name__line product-name__type">INTERIOR</span>
      <span class="product-name__line product-name__main">CLEANER</span>
    </h1>

    <svg class="swoosh" viewBox="0 0 310 740" aria-hidden="true">
      <defs>
        <linearGradient id="band" x1="0" y1="0" x2="1" y2="0">
          <stop offset="0" stop-color="#e54698"/>
          <stop offset=".6" stop-color="#e96aad"/>
          <stop offset="1" stop-color="#f1a4ce"/>
        </linearGradient>
        <linearGradient id="streak" x1="0" y1="0" x2="1" y2="0">
          <stop offset="0" stop-color="#f9d9ea" stop-opacity="0"/>
          <stop offset=".7" stop-color="#fceff6" stop-opacity=".8"/>
          <stop offset="1" stop-color="#fceff6" stop-opacity=".5"/>
        </linearGradient>
      </defs>
      <path d="M0 588 C90 572 200 545 310 508 L310 632 C210 650 100 662 0 668 Z" fill="url(#band)" opacity=".9"/>
      <path d="M0 600 C100 586 210 560 310 530 L310 548 C210 576 100 600 0 612 Z" fill="url(#streak)"/>
      <path d="M0 652 C100 646 210 632 310 612 L310 622 C210 642 100 656 0 660 Z" fill="#f1a4ce" opacity=".6"/>
    </svg>

    <ul class="benefits">
      <li>NON ACIDIC <span class="soft">FORMULA</span></li>
      <li>INTERIOR <span class="soft">AND</span> EXTERIOR</li>
      <li>REMOVES <span class="soft">GREASE GRIME</span> &amp; DIRT</li>
    </ul>

    <p class="net-contents">NET CONTENTS: 16 FL. OZ. (473ML)</p>
  </section>
</body>
</html>
```